Update our insurance company Business Card

Create a more current card with two locations. Ashford Ridge & Marlow Bay. Please make suggestions for: photo or no photos, back of card, type of material etc. We are risk advisors / insurance brokers and cater to businesses and the affluent home owner. We have been in a luxury resort community for 8 years and are expanding to a second location in Ashford Ridge.

Target Market(s)

We are risk advisors / insurance brokers and cater to businesses (Tech, Healthcare, Restaurants, Hotels, Commercial property) and the affluent home owner. We have been in a luxury resort community for 8 years and are expanding to a second location in Ashford Ridge.

Industry/Entity Type

Insurance

Contact Information for Business Card

Tavish K. Merriam, CLCS
President & CEO

Marlow Bay: 555-014-2267
Ashford Ridge: TBD
Fax: 555-014-2268
E-Mail: Tavish@mwcoverageteam.com

Website: www.mwcoverageteam.com

Colors

Designer to choose colors to be used in the design.

Requirements
Must have
• LOGO. I will need phone #'s for Ashford Ridge, Marlow Bay, Mobile, and Fax. Website and e-mail. Must have cropped photo chest up or face.
Nice to have
• Please make suggestions for: QR Code or something better, photo, back of card, type of material etc. Red edging. See file.

```html
<!DOCTYPE html>
<html lang="en">
<head>
<meta charset="utf-8">
<title>M &amp; W Coverage Team – Business Card</title>
<link rel="stylesheet" href="https://fonts.googleapis.com/css2?family=Open+Sans:wght@400;700&family=Oswald:wght@500&display=swap">
<style>
  :root {
    --stage: #a7a7a7;
    --card-black: #040404;
    --band: #101010;
    --back-grey: #2b2b2b;
    --red: #ff1a14;
    --red-mid: #cc0000;
    --red-deep: #990000;
    --white: #ffffff;
  }
  * { margin: 0; padding: 0; box-sizing: border-box; }
  html, body { width: 960px; height: 1200px; overflow: hidden; }
  body { background: var(--stage); font-family: "Open Sans", Arial, sans-serif; position: relative; }

  .card { position: absolute; left: 27px; width: 900px; height: 540px; overflow: hidden; }
  .card-front { top: 48px; background: var(--card-black); }
  .card-back { top: 622px; background: var(--back-grey); }
  .card-art { position: absolute; inset: 0; width: 900px; height: 540px; }

  .logo-band { position: absolute; left: 0; top: 166px; width: 510px; height: 82px; background: var(--band); }

  .wordmark { position: absolute; color: var(--red); font-weight: 700; text-transform: uppercase; text-align: center; line-height: 1; }
  .wordmark .mark-initials { display: block; font-size: 84px; letter-spacing: 4px; }
  .wordmark .mark-name { display: block; font-size: 25px; letter-spacing: 1px; margin-top: 6px; }
  .card-front .wordmark { left: 70px; top: 70px; width: 400px; }
  .card-back .wordmark { left: 264px; top: 180px; width: 400px; }

  .contact-list { position: absolute; left: 0; top: 0; list-style: none; }
  .contact-item { position: absolute; left: 52px; display: flex; align-items: center; width: 460px; }
  .contact-icon { width: 38px; height: 38px; flex: none; }
  .contact-text { margin-left: 27px; color: var(--white); font-size: 21px; line-height: 29px; white-space: nowrap; }
  .item-phone { top: 248px; }
  .item-web { top: 349px; }
  .item-mail { top: 402px; }

  .person { position: absolute; left: 526px; top: 228px; width: 340px; text-align: center; color: var(--red); }
  .person-name { font-family: "Oswald", "Arial Narrow", sans-serif; font-weight: 500; font-size: 32px; letter-spacing: -0.5px; line-height: 42px; white-space: nowrap; }
  .person-title { font-size: 27px; line-height: 36px; margin-top: 6px; }
</style>
</head>
<body>

<section class="card card-front">
  <svg class="card-art" viewBox="0 0 900 540" aria-hidden="true">
    <defs>
      <clipPath id="crescent-span"><rect x="0" y="76" width="900" height="368"/></clipPath>
      <clipPath id="disc-shape"><ellipse cx="822" cy="264" rx="292" ry="340"/></clipPath>
      <linearGradient id="crescent-fill" x1="0" y1="0" x2="0" y2="1">
        <stop offset="0" stop-color="#ff1a14"/>
        <stop offset="0.5" stop-color="#c40000"/>
        <stop offset="1" stop-color="#8a0000"/>
      </linearGradient>
    </defs>
    <ellipse cx="800" cy="264" rx="296" ry="340" fill="url(#crescent-fill)" clip-path="url(#crescent-span)"/>
    <ellipse cx="822" cy="264" rx="292" ry="340" fill="#050505"/>
    <g clip-path="url(#disc-shape)">
      <rect x="560" y="446" width="153" height="56" fill="var(--red)"/>
      <rect x="685" y="446" width="104" height="56" fill="var(--red-mid)"/>
      <rect x="789" y="446" width="111" height="56" fill="var(--red-deep)"/>
    </g>
  </svg>

  <div class="logo-band"></div>
  <div class="wordmark">
    <span class="mark-initials">M &amp; W</span>
    <span class="mark-name">Coverage Team LLC</span>
  </div>

  <ul class="contact-list">
    <li class="contact-item item-phone">
      <svg class="contact-icon" viewBox="0 0 38 38" aria-hidden="true">
        <circle cx="19" cy="19" r="19" fill="var(--red)"/>
        <path d="M12 11c1-1 2-1 3 0l2 3c.6 1 .3 1.8-.5 2.5l-1 .8c.8 2 2.4 3.7 4.4 4.6l.9-1c.7-.8 1.6-1 2.5-.4l3 2c1 .8 1 2 0 3l-1.3 1.3c-1.4 1.3-4 .8-7-1.4-3.2-2.4-5.6-5.6-6.6-8.4-.6-2-.4-3.3.4-4.2z" fill="var(--card-black)"/>
      </svg>
      <span class="contact-text">Marlow Bay: 555-014-2267<br>Ashford Ridge: TBD<br>FAX: 555-014-2268</span>
    </li>
    <li class="contact-item item-web">
      <svg class="contact-icon" viewBox="0 0 38 38" aria-hidden="true">
        <circle cx="19" cy="19" r="19" fill="var(--red)"/>
        <circle cx="19" cy="19" r="9" fill="none" stroke="var(--card-black)" stroke-width="2"/>
        <path d="M10 19h18M19 10c-3 3-3 15 0 18M19 10c3 3 3 15 0 18" fill="none" stroke="var(--card-black)" stroke-width="1.8"/>
      </svg>
      <span class="contact-text">www.mwcoverageteam.com</span>
    </li>
    <li class="contact-item item-mail">
      <svg class="contact-icon" viewBox="0 0 38 38" aria-hidden="true">
        <circle cx="19" cy="19" r="19" fill="var(--red)"/>
        <rect x="10" y="13" width="18" height="12" fill="var(--card-black)"/>
        <path d="M10.5 13.5l8.5 6.5 8.5-6.5M10.5 24.5l6-5M27.5 24.5l-6-5" fill="none" stroke="var(--red)" stroke-width="1.4"/>
      </svg>
      <span class="contact-text">Tavish@mwcoverageteam.com</span>
    </li>
  </ul>

  <div class="person">
    <p class="person-name">TAVISH K. MERRIAM, CLCS</p>
    <p class="person-title">President &amp; CEO</p>
  </div>
</section>

<section class="card card-back">
  <svg class="card-art" viewBox="0 0 900 540" aria-hidden="true">
    <defs>
      <clipPath id="back-arc-span"><rect x="0" y="76" width="900" height="372"/></clipPath>
      <linearGradient id="back-arc-fill" x1="0" y1="0" x2="0" y2="1">
        <stop offset="0" stop-color="#ff1a14"/>
        <stop offset="0.55" stop-color="#c00000"/>
        <stop offset="1" stop-color="#9a0000"/>
      </linearGradient>
    </defs>
    <ellipse cx="453" cy="264" rx="305" ry="330" fill="url(#back-arc-fill)" clip-path="url(#back-arc-span)"/>
    <ellipse cx="453" cy="264" rx="282" ry="340" fill="#161616"/>
  </svg>
  <div class="wordmark">
    <span class="mark-initials">M &amp; W</span>
    <span class="mark-name">Coverage Team LLC</span>
  </div>
</section>

</body>
</html>
```